Commercial photographer, UAV drone photography & 360 walk-through visuals

I need a business card design that is minimalist but yet pretentiously creative. My target market are architects, designers, advertising agents and marketing managers. It is important to stress that though I am asking for a minimalist design it needs to have creative impact.

Target Market(s)

Architects, interiors designers, web-designers, artists

Contact Information for Business Card

Include my name, mobile [cell] number, email, web page and the company logo. Do not to include a postal address.

Colors

Designer to choose colors to be used in the design.

Requirements
Must have
• The following information is to be included:
• Milo Fenwick
• Photographer
• m: 07812 593174
• e: milo@mfimagery.co.uk
• w: mfimagery.co.uk

```html
<!DOCTYPE html>
<html lang="en">
<head>
<meta charset="utf-8">
<title>MF Imagery – Business Card</title>
<link href="https://fonts.googleapis.com/css2?family=Lato:wght@300;400;700&display=swap" rel="stylesheet">
<style>
  :root {
    --backdrop: #2b2b2d;
    --card: #1d1d1f;
    --ink: #f4f4f4;
    --ink-muted: #a9a9ab;
    --rule: #6a6a6c;
  }
  * { margin: 0; padding: 0; box-sizing: border-box; }
  html, body {
    width: 1200px;
    height: 1108px;
    overflow: hidden;
    background: var(--backdrop);
    font-family: "Lato", sans-serif;
  }
  .canvas {
    position: relative;
    width: 1200px;
    height: 1108px;
    display: flex;
    justify-content: center;
    align-items: center;
    gap: 60px;
  }
  .card {
    position: relative;
    width: 400px;
    height: 640px;
    background: var(--card);
    border-radius: 26px;
    color: var(--ink);
  }
  .wordmark {
    display: flex;
    align-items: center;
    gap: 14px;
    font-weight: 400;
    text-transform: uppercase;
    color: var(--ink);
    line-height: 1;
  }
  .wordmark-dot {
    border-radius: 50%;
    background: var(--ink);
    flex: none;
  }
  /* front */
  .card-front .wordmark {
    position: absolute;
    left: 48px;
    top: 86px;
    font-size: 34px;
    letter-spacing: 6px;
  }
  .card-front .wordmark-dot { width: 18px; height: 18px; }
  .identity {
    position: absolute;
    left: 0;
    right: 0;
    top: 330px;
    text-align: center;
  }
  .person-name {
    font-size: 22px;
    font-weight: 400;
    letter-spacing: 1.5px;
    text-transform: uppercase;
  }
  .person-role {
    margin-top: 4px;
    font-size: 15px;
    font-weight: 300;
    letter-spacing: 1.5px;
    color: var(--ink-muted);
    text-transform: uppercase;
  }
  .divider {
    margin: 10px auto 0;
    width: 190px;
    display: flex;
    align-items: center;
    gap: 6px;
  }
  .divider-line { flex: 1; height: 1px; background: var(--rule); }
  .divider-icon {
    width: 16px; height: 16px;
    border-radius: 50%;
    background: var(--ink);
    display: flex; align-items: center; justify-content: center;
  }
  .contact-list {
    list-style: none;
    margin-top: 12px;
    font-size: 15px;
    font-weight: 300;
    line-height: 1.4;
    color: var(--ink-muted);
    letter-spacing: 0.5px;
  }
  /* back */
  .card-back .wordmark {
    position: absolute;
    left: 48px;
    bottom: 70px;
    font-size: 46px;
    letter-spacing: 8px;
  }
  .card-back .wordmark-dot { width: 22px; height: 22px; }
</style>
</head>
<body>
  <main class="canvas">
    <section class="card card-front" aria-label="Card front">
      <div class="wordmark"><span class="wordmark-dot"></span>MF Imagery</div>
      <div class="identity">
        <h1 class="person-name">Milo Fenwick</h1>
        <p class="person-role">Photographer</p>
        <div class="divider">
          <span class="divider-line"></span>
          <span class="divider-icon" aria-label="Phone">
            <svg width="10" height="10" viewBox="0 0 10 10"><path d="M2 1.2 3.4 1l.8 2-.9.7a5 5 0 0 0 2 2l.7-.9 2 .8-.2 1.4C6.9 8 1.9 4.2 2 1.2z" fill="#1d1d1f"/></svg>
          </span>
          <span class="divider-icon" aria-label="Email">
            <svg width="10" height="10" viewBox="0 0 10 10"><rect x="1.5" y="2.5" width="7" height="5" fill="none" stroke="#1d1d1f" stroke-width="1"/><path d="M1.5 2.5 5 5.5l3.5-3" fill="none" stroke="#1d1d1f" stroke-width="1"/></svg>
          </span>
          <span class="divider-icon" aria-label="Website">
            <svg width="10" height="10" viewBox="0 0 10 10"><circle cx="5" cy="5" r="3.5" fill="none" stroke="#1d1d1f" stroke-width="1"/><path d="M1.5 5h7M5 1.5c-2 2-2 5 0 7M5 1.5c2 2 2 5 0 7" fill="none" stroke="#1d1d1f" stroke-width=".8"/></svg>
          </span>
          <span class="divider-line"></span>
        </div>
        <ul class="contact-list">
          <li>07812 593174</li>
          <li>milo@mfimagery.co.uk</li>
          <li>www.mfimagery.co.uk</li>
        </ul>
      </div>
    </section>

    <section class="card card-back" aria-label="Card back">
      <div class="wordmark"><span class="wordmark-dot"></span>MF Imagery</div>
    </section>
  </main>
</body>
</html>
```